Surgical Procedure Room Letterhead

PLEASE DO NOT MAKE YOUR LETTERHEAD SIMILAR TO THE ONE I AM INCLUDING IN MY UPLOADS

Hello! I need my logo used to make a very clean, professional, simple letterhead that has all the pertinent information in it:
Location: 4829 NW 58th Lane, Suite 310
Tamarac, FL 33468
Phone: 954-618-2450
Fax: 800-394-8261

Can you please put this all on a word document that is easily editable? I will include my practice letterhead as an example ONLY of how easy it should be to write below the letterhead. Please don't make this letterhead the same as the one I am including in this example. They are two separate businesses.

Target Market(s)

Insurance companies

Industry/Entity Type

medical

Requirements
Must have
• classiness, elegance, simplicity
Should not have
• Please don't make your letterhead the same as the one that I included in my uploads

```html
<!DOCTYPE html>
<html lang="en">
<head>
<meta charset="utf-8">
<title>Meridian Surgical Suites Letterhead</title>
<link rel="stylesheet" href="https://fonts.googleapis.com/css2?family=Roboto:wght@400;500&display=swap">
<style>
  :root {
    --backdrop: #dcdcdc;
    --paper: #f8f8f8;
    --navy: #14284b;
    --gold: #c9a233;
    --ink: #3a3a3a;
    --rule: #c9b48a;
  }
  * { margin: 0; padding: 0; box-sizing: border-box; }
  html, body {
    width: 1153px;
    height: 1200px;
    overflow: hidden;
    background: var(--backdrop);
    font-family: "Roboto", Arial, sans-serif;
  }
  .letterhead {
    position: absolute;
    left: 166px;
    top: 30px;
    width: 820px;
    height: 1140px;
    background: var(--paper);
    box-shadow: 0 6px 18px rgba(0,0,0,0.12);
  }
  .masthead {
    position: absolute;
    left: 61px;
    top: 63px;
    display: flex;
    align-items: center;
    height: 58px;
  }
  .brand {
    display: flex;
    align-items: center;
    gap: 8px;
    width: 217px;
  }
  .brand-dot {
    width: 14px;
    height: 14px;
    border-radius: 50%;
    background: var(--gold);
    flex: none;
  }
  .brand-name {
    font-weight: 500;
    font-size: 17px;
    line-height: 19px;
    color: var(--navy);
    letter-spacing: 0.3px;
  }
  .divider {
    width: 1px;
    height: 58px;
    background: var(--rule);
    margin-right: 11px;
  }
  .contact {
    font-size: 13px;
    line-height: 16px;
    color: var(--ink);
  }
  .contact-lines { display: flex; gap: 8px; margin-top: 1px; }
  .contact-item { display: flex; align-items: center; gap: 5px; }
  .contact-item svg { width: 12px; height: 12px; fill: var(--navy); }
</style>
</head>
<body>
  <main class="letterhead">
    <header class="masthead">
      <div class="brand">
        <span class="brand-dot"></span>
        <span class="brand-name">Meridian<br>Surgical Suites</span>
      </div>
      <div class="divider"></div>
      <address class="contact" style="font-style:normal">
        <div>4829 NW 58th Lane,</div>
        <div>Suite 310 Tamarac, FL 33468</div>
        <div class="contact-lines">
          <span class="contact-item">
            <svg viewBox="0 0 12 12" aria-hidden="true"><path d="M1 4c0-1.5 2.5-2.5 5-2.5s5 1 5 2.5v1H8.5V3.8H3.5V5H1z"/><path d="M3 6l1.5-1.5h3L9 6v5H3z"/><circle cx="6" cy="8" r="1.3" fill="#f8f8f8"/></svg>
            954-618-2450
          </span>
          <span class="contact-item">
            <svg viewBox="0 0 12 12" aria-hidden="true"><rect x="3" y="1" width="6" height="4"/><rect x="1" y="5" width="10" height="5" rx="1"/><rect x="3" y="7" width="6" height="1" fill="#f8f8f8"/></svg>
            800-394-8261
          </span>
        </div>
      </address>
    </header>
  </main>
</body>
</html>
```